TRV Mechanical Solutions Business Card Design

Business card design

Thinking just large logo on one side with a phone number and the back side is contact info with services we offer with a industrial plant across the bottom of the card

See must haves. I will be laser etching these business cards on black metal business cards as well as full color card stock. So must be bold and professional.

Target Market(s)

Industrial manufacturing

Contact Information for Business Card

Industrial manufacturing construction business specializing in consulting project managment and completing projects turn key

Font styles to use
Other font styles liked:
• See Logo for colors and font style

Requirements
Must have
• TRV Mechanical Solutions
• Gerald Munroe
• 2847 Alderwick Lane
• Bel Air, MD, 21047
• Project Managment
• Consulting
• Turn Key Industrial Projects
• I’d like a industrial manufacturing “cityline” on the back side bottom of the
• I’d like to be able to print these business cards in regular color on card stock but I’d also like the design to be etched into black metal business cards

```html
<!DOCTYPE html>
<html lang="en">
<head>
<meta charset="utf-8">
<title>TRV Mechanical Solutions – Business Card</title>
<link rel="stylesheet" href="https://fonts.googleapis.com/css2?family=Lato:wght@400;700;900&family=Exo+2:wght@700&display=swap">
<style>
  :root {
    --bg: #5b5b5b;
    --card: #ffffff;
    --brand-blue: #2d55a8;
    --ink-dark: #3a3a3a;
    --ink-body: #333333;
    --divider: #e2e2e2;
    --skyline-top: #ffffff;
    --skyline-bottom: #e6e6e6;
    --band-text: #ffffff;
  }
  * { margin: 0; padding: 0; box-sizing: border-box; }
  html, body { width: 1200px; height: 802px; overflow: hidden; }
  body {
    background: var(--bg);
    position: relative;
    font-family: "Lato", sans-serif;
  }
  .card {
    position: absolute;
    top: 274px;
    width: 443px;
    height: 265px;
    background: var(--card);
    overflow: hidden;
    box-shadow: 0 3px 8px rgba(0,0,0,.35);
  }
  .card--front { left: 136px; }
  .card--back { left: 624px; }

  .band {
    position: absolute;
    left: 0; right: 0; bottom: 0;
    height: 42px;
    background: var(--brand-blue);
    color: var(--band-text);
    display: flex;
    align-items: center;
    justify-content: center;
  }

  /* Front */
  .brand-mark {
    position: absolute;
    left: 45px;
    top: 103px;
    width: 160px;
    display: flex;
    align-items: center;
    gap: 8px;
    color: var(--brand-blue);
    font-weight: 900;
    font-size: 17px;
    line-height: 1.15;
  }
  .brand-mark__square {
    flex: none;
    width: 14px; height: 14px;
    background: var(--brand-blue);
  }
  .divider {
    position: absolute;
    left: 227px; top: 77px;
    width: 1px; height: 120px;
    background: var(--divider);
  }
  .contact {
    position: absolute;
    left: 251px;
    top: 91px;
  }
  .contact__name {
    font-weight: 900;
    font-size: 16.5px;
    letter-spacing: .2px;
    color: var(--ink-dark);
    text-transform: uppercase;
  }
  .contact__name .first { color: var(--brand-blue); }
  .contact__address {
    margin-top: 30px;
    font-size: 13px;
    line-height: 16px;
    color: var(--ink-body);
  }
  .services {
    font-size: 12.8px;
    letter-spacing: .1px;
  }
  .services .sep { margin: 0 6px; }

  /* Back */
  .brand-name {
    position: absolute;
    top: 82px;
    left: 0; right: 0;
    text-align: center;
    color: var(--brand-blue);
    font-weight: 900;
    font-size: 30px;
    line-height: 1.1;
  }
  .skyline {
    position: absolute;
    left: 0; right: 0; bottom: 42px;
    height: 48px;
    background: linear-gradient(to bottom, var(--skyline-top), var(--skyline-bottom));
  }
  .phone {
    font-family: "Exo 2", sans-serif;
    font-weight: 700;
    font-size: 21px;
    letter-spacing: .6px;
  }
</style>
</head>
<body>

  <section class="card card--front">
    <div class="brand-mark">
      <span class="brand-mark__square"></span>
      <span>TRV Mechanical Solutions</span>
    </div>
    <div class="divider"></div>
    <div class="contact">
      <p class="contact__name"><span class="first">Gerald</span> Munroe</p>
      <p class="contact__address">2847 Alderwick Lane<br>Bel Air, MD, 21047</p>
    </div>
    <div class="band services">
      Project Managment<span class="sep">|</span>Consulting<span class="sep">|</span>Turn Key Industrial Projects
    </div>
  </section>

  <section class="card card--back">
    <p class="brand-name">TRV Mechanical<br>Solutions</p>
    <div class="skyline" role="img" aria-label="Faint grey industrial city skyline silhouette along the bottom of the card"></div>
    <div class="band phone">044-318 672 905</div>
  </section>

</body>
</html>
```